Virtual Assistant/Online Marketing Business Card/Stationary

I need a professional but modern business card/stationary for my company in Dallas called Brivolo. Brivolo is a virtual assistant specializing in online marketing. I would like a unique design that stands out and makes my brand clear. Incorporating the logo is a must and have attached it to this brief.

Target Market(s)

small business owners & entrepreneurs, 35-65

Industry/Entity Type

Business

Contact Information for Business Card

Maren Tolk
marentolk@brivolo.biz
(555) 271-9064
brivolo.biz

Font styles to use
Sans Serif

Colors
f04a50
3176b5
9bcb3c

Requirements
Must have
• Colors that match the logo colors. Logo integration

```html
<!DOCTYPE html>
<html lang="en">
<head>
<meta charset="utf-8">
<title>Brivolo — Business Card</title>
<link rel="stylesheet" href="https://fonts.googleapis.com/css2?family=Noto+Sans:wght@400;700&display=swap">
<style>
  :root {
    --brand-red: #f04a50;
    --brand-blue: #3176b5;
    --brand-green: #9bcb3c;
    --card-dark: #262626;
    --card-white: #ffffff;
    --backdrop: #ece7e1;
    --text-light: #ffffff;
  }
  html, body {
    margin: 0;
    padding: 0;
    width: 1200px;
    height: 902px;
    overflow: hidden;
    background: var(--backdrop);
  }
  .stage {
    position: relative;
    width: 1200px;
    height: 902px;
  }
  .business-card {
    position: absolute;
    left: 370px;
    top: 51px;
    width: 460px;
    height: 800px;
    border-radius: 18px;
    overflow: hidden;
    background: var(--card-white);
    box-shadow: 0 6px 22px rgba(0, 0, 0, 0.18);
    font-family: "Noto Sans", Tahoma, sans-serif;
  }
  .card-shapes {
    position: absolute;
    inset: 0;
  }
  .wordmark {
    position: absolute;
    top: 200px;
    left: 0;
    width: 100%;
    display: flex;
    align-items: center;
    justify-content: center;
    gap: 14px;
  }
  .wordmark-dot {
    width: 34px;
    height: 34px;
    border-radius: 50%;
    background: var(--brand-red);
  }
  .wordmark-name {
    font-size: 78px;
    font-weight: 700;
    color: var(--card-dark);
    letter-spacing: -1px;
    line-height: 1;
  }
  .contact {
    position: absolute;
    top: 496px;
    left: 0;
    width: 100%;
    text-align: center;
  }
  .contact-name {
    margin: 0 0 40px;
    font-size: 30px;
    font-weight: 700;
    color: var(--brand-green);
  }
  .contact-line {
    margin: 0 0 12px;
    font-size: 25px;
    font-weight: 400;
    color: var(--text-light);
  }
  .contact-web {
    color: var(--brand-green);
  }
</style>
</head>
<body>
<main class="stage">
  <section class="business-card" aria-label="Brivolo business card">
    <svg class="card-shapes" width="460" height="800" viewBox="0 0 460 800" aria-hidden="true">
      <path d="M0,372 Q230,490 460,356 L460,440 L0,440 Z" fill="var(--brand-green)"/>
      <path d="M0,392 Q230,512 460,380 L460,800 L0,800 Z" fill="var(--card-dark)"/>
    </svg>

    <div class="wordmark">
      <span class="wordmark-dot"></span>
      <span class="wordmark-name">Brivolo</span>
    </div>

    <div class="contact">
      <p class="contact-name">Maren Tolk</p>
      <p class="contact-line">(555) 271-9064</p>
      <p class="contact-line">marentolk@brivolo.biz</p>
      <p class="contact-line contact-web">brivolo.biz</p>
    </div>
  </section>
</main>
</body>
</html>
```